Plumbing Trifold Design for Restoration Company

We would like this brochure to match our current KVT branding and marketing materials. The overall look should feel modern, clean, premium, and trustworthy.

Our brand colors are included in the attached files along with a picture of what our current marketing material looks like. We'd like to use real KVT photography whenever possible rather than stock images, but if stock images are necessary, please go ahead and use.

The brochure should communicate that KVT is a full-service plumbing company backed by years of experience in both traditional plumbing and complex pipe restoration.

Front Page: we would like to include logo, phone number (800-318-4957), website (www.kvtflow.example) and then maybe the following: "Traditional Plumbing Services", "residential & commercial, 24/7 Emergency Service, Licensed & Insured" and can also add "reliable Repairs. Honest Service. Lasting Solutions" if spacing allows.

Other sections we would like included (not in any particular order):

-Why Choose KVT?:
Family-oriented team
Licensed & insured professionals
Residential & commercial expertise
Honest recommendations
Quality workmanship
Emergency service available
Clean, respectful technicians
One trusted company for plumbing and sewer solutions
____________________________
Our Story:
Built on solving complex plumbing challenges. Trusted for every plumbing need.
Since our founding, Conduit Renewal Partners has built a reputation for helping homeowners, businesses, and property managers solve some of the industry’s most challenging plumbing and sewer problems through quality workmanship, professionalism, and innovative solutions.
As our customers’ needs have grown, so has our commitment to serving them. What began as a leader in pipe restoration has expanded into full-service plumbing, allowing us to provide complete plumbing solutions—from everyday repairs and fixture replacements to water heaters, drain cleaning, repiping, and emergency plumbing services.
Today, our traditional plumbing division delivers the same level of expertise, communication, and customer care that KVT has become known for. Whether it’s a simple repair or a complex plumbing project, our goal remains the same: to provide dependable solutions, lasting quality, and an exceptional customer experience every step of the way.
-Our Values:
The KVT Way
Professional - Don't settle for good, BE GREAT
Responsive - When there's a need, BE FIRST!
Service - Life is not about you, BE ABOUT OTHERS!
These three values guide everything we do
Complete Plumbing Solutions:
-Plumbing Repairs
Reliable solutions to keep your plumbing system running safely and efficiently.
Leak detection & repair
Pipe Burst Repairs
Water line repairs
Whole-home repiping

-Fixtures & Installations
Professional installation, repair, and replacement of the fixtures you use every day.
Faucets
Toilets
Sinks
Showers & tubs
Garbage disposals
Hose bibs
Shut-off valves

-Water Heater Services
Whether you need a repair, replacement, or routine maintenance, we'll keep your hot water flowing.
Water heater repair
Water heater replacement
Tankless water heaters
Expansion tanks
Recirculation pumps
Preventative maintenance

-Drain & Sewer Solutions
From routine drain cleaning to complete sewer repairs, our team has the equipment and expertise to get your plumbing flowing again.
Drain cleaning
Hydro jetting
Camera inspections
Main sewer line cleaning
Sewer line repair
Sewer line replacement
Emergency drain backups
maybe add in a blurb saying
"Need a Trenchless Solution?
Ask about our non-invasive solutions as an alternative to traditional replacement for sewer and storm drain systems"
Testimonials:
"This company is fantastic, very professional and knowledgeable. Use them at several of my communities I manage and highly recommend them!" Belvine Townhomes
"KVT continues to be the primary plumbing vendor I use for all of my properties throughout Tampa Bay!" Corliss Dunes Condominium
"KVT did a great job at a great price and have always been willing to help with their abundance of knowledge prior to even working on projects for our community!" Townhomes at Hollow Fern
"KVT is amazing! My office flooded out on a Friday night and they responded within a couple hours to make the needed repair. The team was professional and got right to work (there van was also immaculate, which tells you a lot about hot they operate). Would definitely recommend them to anyone!" Dorin Welsby
______________________
Ready to get started?
Whether it's a leaking pipe, a new water heater, a clogged drain, or a plumbing emergency, our team is here to help
800-318-4957
info@kvtflow.example
www.kvtflow.example

Additional Information: please feel free to edit any of the pictures provided and AI files can be provided for the other marketing material if helpful. We would like an AI file and PDF ready print if possible.
Thank you!

commercial and residential property owners

Plumbing

Colors
0054AA
0677BA
7BADD7
CADEEF
E8F1F8

Must have
• My project must flow with current marketing material colors
Nice to have
• would like the front page picture to fade nicely into background

```html
<!DOCTYPE html>
<html lang="en">
<head>
<meta charset="utf-8">
<title>KVT Trifold – Outside Spread</title>
<link rel="stylesheet" href="https://fonts.googleapis.com/css2?family=Poppins:wght@700&family=Questrial&family=Kalam:wght@400&display=swap">
<style>
  :root{
    --brand-deep:#0054AA;
    --brand-blue:#0677BA;
    --brand-sky:#7BADD7;
    --brand-mist:#CADEEF;
    --brand-ice:#E8F1F8;
    --heading:#1E94D6;
    --navy:#2B3566;
    --body:#5d6066;
    --paper:#ffffff;
    --backdrop:#d6d8db;
  }
  *{box-sizing:border-box;margin:0;padding:0}
  html,body{width:1200px;height:820px;overflow:hidden;background:var(--backdrop)}
  .sheet{position:relative;width:1200px;height:820px;background:var(--paper);overflow:hidden;font-family:"Questrial",sans-serif;color:var(--body)}
  .waves{position:absolute;left:0;width:1200px;height:110px}
  .waves--top{top:0}
  .waves--bottom{bottom:0}
  .panel{position:absolute;top:0;height:820px;width:400px}
  .panel--contact{left:0}
  .panel--story{left:400px}
  .panel--cover{left:800px}
  .headline{font-family:"Poppins",sans-serif;font-weight:700;color:var(--heading);line-height:1.14}
  .contact__title{position:absolute;left:41px;top:62px;font-size:31px}
  .contact__intro{position:absolute;left:41px;top:150px;width:330px;font-size:14.5px;line-height:20px}
  .contact__list{position:absolute;left:41px;top:232px;list-style:none}
  .contact__list li{display:flex;align-items:center;height:42px;font-size:15px;color:var(--heading)}
  .contact__list svg{width:28px;height:28px;margin-right:34px}
  .photo{position:absolute;border-radius:50%}
  .photo--van{left:42px;top:387px;width:322px;height:322px;border:9px solid var(--brand-deep);
    background:radial-gradient(circle at 50% 32%,#d9c6a8 0 22%,#9fb59a 38%,#f2f4f6 55%,#6b6f75 78%,#4a4d52 100%);
    box-shadow:0 0 0 3px var(--brand-blue)}
  .story__title{position:absolute;left:17px;top:52px;font-size:33.5px}
  .story__script{position:absolute;left:22px;top:176px;font-family:"Kalam",cursive;font-size:22px;color:var(--navy);transform:skewX(-8deg)}
  .story__text{position:absolute;left:17px;width:368px;font-size:15px;line-height:19px;letter-spacing:.5px;text-align:justify}
  .story__text--one{top:222px}
  .story__text--two{top:410px}
  .checklist{position:absolute;left:17px;top:516px;list-style:none}
  .checklist li{display:flex;align-items:flex-start;min-height:32.4px;font-size:14px;line-height:15px;color:var(--heading)}
  .checklist svg{width:30px;height:26px;margin-right:20px;flex:none;margin-top:-6px}
  .checklist span{padding-top:2px;width:250px}
  .brand{position:absolute;left:85px;top:52px;width:235px;text-align:center;font-family:"Poppins",sans-serif;font-weight:700;font-size:50px;line-height:1;color:var(--navy);letter-spacing:6px}
  .photo-frame{position:absolute;left:22px;top:148px;width:326px;height:326px}
  .photo-frame__accent{position:absolute;left:12px;top:0;width:316px;height:316px;border-radius:50%;background:var(--brand-blue)}
  .photo--pipes{left:0;top:0;width:316px;height:316px;border:12px solid var(--navy);
    background:linear-gradient(160deg,#e9eef6 0 45%,#c7d3e4 60%,#7a5a48 72%,#4c9ec4 82%,#9a3a2e 100%)}
  .cover__title{position:absolute;left:32px;top:491px;font-size:31.5px;line-height:39px}
  .features{position:absolute;left:45px;top:575px;list-style:none}
  .features li{display:flex;align-items:center;height:37px;font-size:15px;color:var(--body)}
  .features svg{width:26px;height:26px;margin-right:12px}
  .cover__tagline{position:absolute;left:36px;top:686px;font-family:"Kalam",cursive;font-size:13.5px;color:var(--navy);transform:skewX(-8deg);word-spacing:3px}
  .cover__footer{position:absolute;left:40px;top:748px;display:flex;align-items:center;font-size:14.5px;color:var(--body)}
  .cover__footer svg{width:24px;height:24px;margin-right:22px}
  .cover__footer .divider{width:1px;height:18px;background:var(--body);margin:0 12px}
</style>
</head>
<body>
<main class="sheet">
  <svg class="waves waves--top" viewBox="0 0 1200 110" preserveAspectRatio="none" aria-hidden="true">
    <path d="M0 0H1200V92C1050 58 930 40 780 70C620 100 520 95 420 70C300 42 150 60 0 88Z" fill="var(--brand-mist)"/>
    <path d="M0 0H1200V48C1080 78 960 52 820 36C660 18 520 58 380 46C240 34 120 28 0 50Z" fill="var(--brand-sky)"/>
    <path d="M0 0H1200V18C1060 12 930 30 800 24C640 16 560 0 400 18C260 34 120 40 0 26Z" fill="#4A8FD0"/>
  </svg>
  <svg class="waves waves--bottom" viewBox="0 0 1200 110" preserveAspectRatio="none" aria-hidden="true">
    <path d="M0 110H1200V22C1060 46 940 56 780 34C630 14 520 8 400 26C260 46 130 40 0 14Z" fill="var(--brand-mist)"/>
    <path d="M0 110H1200V62C1080 38 960 50 820 66C660 84 520 58 380 60C240 62 120 70 0 52Z" fill="var(--brand-sky)"/>
    <path d="M0 110H1200V82C1060 92 920 70 780 76C630 82 540 102 400 90C260 78 130 72 0 84Z" fill="#4A8FD0"/>
  </svg>

  <section class="panel panel--contact">
    <h2 class="headline contact__title">Ready to get<br>started?</h2>
    <p class="contact__intro">Whether it's a leaking pipe, a new water heater, a clogged drain, or a plumbing emergency, our team is here to help</p>
    <ul class="contact__list">
      <li><svg viewBox="0 0 24 24" fill="none" stroke="var(--brand-blue)" stroke-width="1.4"><path d="M5 3h4l2 5-2.5 1.5a11 11 0 0 0 6 6L16 13l5 2v4a2 2 0 0 1-2 2A16 16 0 0 1 3 5a2 2 0 0 1 2-2z"/></svg>800-318-4957</li>
      <li><svg viewBox="0 0 24 24" fill="none" stroke="var(--brand-blue)" stroke-width="1.4"><circle cx="12" cy="12" r="9"/><path d="M3 12h18M12 3c3 3 3 15 0 18M12 3c-3 3-3 15 0 18M5 7h14M5 17h14"/></svg>info@kvtflow.example</li>
      <li><svg viewBox="0 0 24 24" fill="none" stroke="var(--brand-blue)" stroke-width="1.4"><path d="M3 10l9-6 9 6v10H3z"/><path d="M3 10l9 6 9-6"/><circle cx="12" cy="9" r="2.5"/></svg>www.kvtflow.example</li>
    </ul>
    <div class="photo photo--van" role="img" aria-label="Photo of a white KVT service van parked in front of a condominium building"></div>
  </section>

  <section class="panel panel--story">
    <h2 class="headline story__title">Built on Solving<br>Complex Plumbing<br>Challenges.</h2>
    <p class="story__script">Trusted for Every Plumbing Need</p>
    <p class="story__text story__text--one">KVT began as a leader in pipe restoration, solving complex plumbing and sewer challenges with innovative technology and expert craftsmanship. Today, we've expanded into complete plumbing services, providing everything from everyday repairs and water heaters to drain cleaning, repiping, emergency plumbing, and advanced sewer solutions.</p>
    <p class="story__text story__text--two">No matter the project, we deliver dependable workmanship, honest service, and lasting solutions our customers can trust.</p>
    <ul class="checklist">
      <li><svg viewBox="0 0 30 26"><rect x="2" y="6" width="18" height="18" rx="2" fill="none" stroke="var(--brand-deep)" stroke-width="2.5"/><path d="M6 14l5 5L27 3" fill="none" stroke="var(--heading)" stroke-width="3.5" stroke-linecap="round"/></svg><span>Family-oriented team</span></li>
      <li><svg viewBox="0 0 30 26"><rect x="2" y="6" width="18" height="18" rx="2" fill="none" stroke="var(--brand-deep)" stroke-width="2.5"/><path d="M6 14l5 5L27 3" fill="none" stroke="var(--heading)" stroke-width="3.5" stroke-linecap="round"/></svg><span>Licensed &amp; insured professionals</span></li>
      <li><svg viewBox="0 0 30 26"><rect x="2" y="6" width="18" height="18" rx="2" fill="none" stroke="var(--brand-deep)" stroke-width="2.5"/><path d="M6 14l5 5L27 3" fill="none" stroke="var(--heading)" stroke-width="3.5" stroke-linecap="round"/></svg><span>Residential &amp; commercial expertise</span></li>
      <li><svg viewBox="0 0 30 26"><rect x="2" y="6" width="18" height="18" rx="2" fill="none" stroke="var(--brand-deep)" stroke-width="2.5"/><path d="M6 14l5 5L27 3" fill="none" stroke="var(--heading)" stroke-width="3.5" stroke-linecap="round"/></svg><span>Honest recommendations</span></li>
      <li><svg viewBox="0 0 30 26"><rect x="2" y="6" width="18" height="18" rx="2" fill="none" stroke="var(--brand-deep)" stroke-width="2.5"/><path d="M6 14l5 5L27 3" fill="none" stroke="var(--heading)" stroke-width="3.5" stroke-linecap="round"/></svg><span>Quality workmanship</span></li>
      <li><svg viewBox="0 0 30 26"><rect x="2" y="6" width="18" height="18" rx="2" fill="none" stroke="var(--brand-deep)" stroke-width="2.5"/><path d="M6 14l5 5L27 3" fill="none" stroke="var(--heading)" stroke-width="3.5" stroke-linecap="round"/></svg><span>Emergency service available</span></li>
      <li><svg viewBox="0 0 30 26"><rect x="2" y="6" width="18" height="18" rx="2" fill="none" stroke="var(--brand-deep)" stroke-width="2.5"/><path d="M6 14l5 5L27 3" fill="none" stroke="var(--heading)" stroke-width="3.5" stroke-linecap="round"/></svg><span>Clean, respectful technicians</span></li>
      <li><svg viewBox="0 0 30 26"><rect x="2" y="6" width="18" height="18" rx="2" fill="none" stroke="var(--brand-deep)" stroke-width="2.5"/><path d="M6 14l5 5L27 3" fill="none" stroke="var(--heading)" stroke-width="3.5" stroke-linecap="round"/></svg><span>One trusted company for plumbing and sewer solutions</span></li>
    </ul>
  </section>

  <section class="panel panel--cover">
    <div class="brand">KVT</div>
    <div class="photo-frame">
      <div class="photo-frame__accent"></div>
      <div class="photo photo--pipes" role="img" aria-label="Photo of lined pipe sections resting on plumbing blueprints"></div>
    </div>
    <h1 class="headline cover__title">Traditional<br>Plumbing Services</h1>
    <ul class="features">
      <li><svg viewBox="0 0 26 26" fill="var(--brand-blue)"><path d="M2 24V8l6-3v19zM9 24V2l7 3v19zM17 24v-9l7 2v7z"/><rect x="11" y="7" width="2" height="2" fill="#fff"/><rect x="11" y="12" width="2" height="2" fill="#fff"/><rect x="19" y="19" width="3" height="5" fill="#fff"/></svg>Residential &amp; commercial</li>
      <li><svg viewBox="0 0 26 26"><circle cx="13" cy="13" r="11" fill="none" stroke="var(--brand-blue)" stroke-width="1.6"/><circle cx="13" cy="13" r="8" fill="var(--brand-blue)"/><text x="13" y="16" font-size="8" font-family="Poppins,sans-serif" font-weight="700" fill="#fff" text-anchor="middle">24</text></svg>24/7 Emergency Service</li>
      <li><svg viewBox="0 0 26 26"><path d="M13 2l10 4v7c0 6-4 10-10 12C7 23 3 19 3 13V6z" fill="var(--brand-blue)"/><path d="M8 13l4 4 7-8" fill="none" stroke="#fff" stroke-width="2.4" stroke-linecap="round"/></svg>Licensed &amp; Insured</li>
    </ul>
    <p class="cover__tagline">Reliable Repairs. Honest Service. Lasting Solutions.</p>
    <div class="cover__footer">
      <svg viewBox="0 0 24 24" fill="var(--brand-deep)"><path d="M5 2h4l2 6-3 2a12 12 0 0 0 6 6l2-3 6 2v4a3 3 0 0 1-3 3A19 19 0 0 1 2 5a3 3 0 0 1 3-3z"/></svg>
      <span>800-318-4957</span><span class="divider"></span><span>www.kvtflow.example</span>
    </div>
  </section>
</main>
</body>
</html>
```